Save The Date for 2019 QRP Symposium

We have an annual meeting each June and need a Save the Date (STD) designed. It should be a two-sided postcard with room for address and stamp (according to US Mail postal standards). I have attached some examples from prior years, but we would appreciate a more modern and attractive design for this year's STD.

Target Market(s)

Our own members - nurses, nurse practitioners, PAs and physicians

Industry/Entity Type

Medical

Requirements
Must have
• Must include our logos (attached), ideally in a coordinating fashion - as was done in prior years (see examples attached) and without modifying the logos too much. Needs have the following information:
• - "Save the Date"
• - "The 12th Annual Vascular Crew Roundtable"
• - "Friday, June 7, 2019" or "6/7/19"
• - "The Halvern–Trask Building | 274 West 19th Street | NYC"
• - Please include our website (www.zq-olm.example/events), phone number (212-555-0147) and email address (ask@zq-olm.example) for people to ask questions
• - Must have space for a postage stamp and the name/address of the postcard recipient
Nice to have
• Would be nice to remain in our blue/grey/olive color palate (see attached Brand Standards guide).
Should not have
• Please do not use stock photos of medical staff. Please don't use cartoons or cartoon images (although a tasteful sketch may be considered).

```html
<!DOCTYPE html>
<html lang="en">
<head>
<meta charset="utf-8">
<title>Save the Date – Vascular Crew Roundtable</title>
<link rel="stylesheet" href="https://fonts.googleapis.com/css2?family=EB+Garamond:ital,wght@0,400;0,500;0,600;1,400&display=swap">
<style>
  :root {
    --page: #e9ebec;
    --paper: #fbfbfb;
    --panel-light: #c3d6e6;
    --panel-mid: #b0c9de;
    --panel-deep: #98b7d2;
    --navy: #1d3561;
    --sketch-light: #a9cde9;
    --sketch-deep: #5f9fcf;
    --veil: rgba(255,255,255,0.72);
  }
  * { box-sizing: border-box; margin: 0; padding: 0; }
  html, body { width: 1200px; height: 960px; overflow: hidden; }
  body {
    background: var(--page);
    font-family: "EB Garamond", Georgia, serif;
    color: var(--navy);
    position: relative;
  }
  .postcard {
    position: absolute;
    left: 240px;
    width: 720px;
    height: 450px;
    background: var(--paper);
    box-shadow: 0 6px 18px rgba(0,0,0,0.12);
  }
  .postcard--front { top: 20px; }
  .postcard--back { top: 490px; }
  .panel {
    position: absolute;
    left: 16px; top: 16px; right: 16px; bottom: 28px;
    background: linear-gradient(100deg, var(--panel-mid) 0%, var(--panel-light) 45%, var(--panel-deep) 100%);
    overflow: hidden;
  }
  .postcard--back .panel { bottom: 16px; }

  /* Front */
  .event-date {
    position: absolute; left: 14px; top: 12px;
    width: 26px; text-align: center;
    font-size: 17px; line-height: 1;
  }
  .event-date span { display: block; padding: 4px 0; }
  .event-date span + span { border-top: 1px solid var(--navy); }
  .sketch {
    position: absolute;
    left: 140px; top: 14px; width: 300px; height: 300px;
    border-radius: 46% 46% 40% 40%;
    background: radial-gradient(ellipse at 50% 55%, var(--sketch-deep) 0%, var(--sketch-light) 50%, rgba(169,205,233,0) 72%);
    opacity: 0.75;
  }
  .headline {
    position: absolute; left: 0; right: 0; top: 112px;
    text-align: center;
  }
  .venue-name { font-size: 18px; margin-left: -30px; }
  .title {
    font-size: 46px; font-weight: 600; letter-spacing: 0.22em;
    line-height: 1.05; margin-top: 2px;
  }
  .title small { font-size: 16px; letter-spacing: 0.24em; vertical-align: middle; margin: 0 10px; }
  .venue-address { font-size: 18px; margin-left: -40px; }
  .event-name {
    margin-top: 14px; font-size: 14px; font-weight: 500;
    letter-spacing: 0.16em; text-transform: uppercase;
  }
  .divider {
    position: absolute; left: 14px; right: 42px; top: 334px;
    border-top: 1.5px solid var(--navy);
  }
  .sponsor {
    position: absolute; display: flex; align-items: center; gap: 8px;
    font-size: 10.5px; line-height: 1.25;
  }
  .sponsor .seal {
    flex: none; width: 34px; height: 34px; border-radius: 50%;
    border: 1.5px solid var(--navy);
  }
  .sponsor em { display: block; font-style: italic; }
  .sponsor--presenter { left: 14px; top: 346px; }
  .sponsor--chapter { left: 170px; top: 358px; }
  .sponsor--center { left: 360px; top: 368px; }
  .contact-line {
    position: absolute; right: 24px; bottom: 9px;
    font-size: 10px; font-style: italic;
  }

  /* Back */
  .sketch--faint {
    left: 90px; top: 20px; width: 380px; height: 380px;
    opacity: 0.35;
  }
  .message-area {
    position: absolute; left: 34px; top: 16px; width: 300px; height: 370px;
    background: var(--veil);
  }
  .stamp-box {
    position: absolute; right: 18px; top: 18px; width: 66px; height: 80px;
    border: 1.5px dashed var(--paper);
    display: flex; align-items: center; justify-content: center;
    font-size: 9px; letter-spacing: 0.14em; text-transform: uppercase;
    color: var(--paper); text-align: center; line-height: 1.3;
  }
  .address-lines {
    position: absolute; left: 380px; top: 150px; width: 280px;
  }
  .address-lines span {
    display: block; height: 14px; background: var(--paper); margin-bottom: 14px;
  }
</style>
</head>
<body>

<section class="postcard postcard--front" aria-label="Postcard front">
  <div class="panel">
    <div class="event-date"><span>06</span><span>07</span><span>19</span></div>
    <div class="sketch" role="img" aria-label="Engraved-style sketch of an anatomical heart wrapped in roses and leaves"></div>
    <div class="headline">
      <p class="venue-name">The Halvern–Trask Building</p>
      <h1 class="title">SAVE<small>THE</small>DATE</h1>
      <p class="venue-address">274 West 19th Street, NYC</p>
      <p class="event-name">The 12th Annual Vascular Crew Roundtable</p>
    </div>
    <div class="divider"></div>
    <div class="sponsor sponsor--presenter">
      <span class="seal"></span>
      <p><em>Presented by</em>The Harbor City<br>Vascular Guild, Inc.</p>
    </div>
    <div class="sponsor sponsor--chapter">
      <span class="seal"></span>
      <p><em>of the</em>Eastshore Chapter,<br>Collegium of Vascular Care</p>
    </div>
    <div class="sponsor sponsor--center">
      <span class="seal"></span>
      <p><em>In association with</em>Lindenfield Heart Center</p>
    </div>
  </div>
  <p class="contact-line">For additional information call 212.555.0147, email ask@zq-olm.example or visit www.zq-olm.example/events</p>
</section>

<section class="postcard postcard--back" aria-label="Postcard back">
  <div class="panel">
    <div class="sketch sketch--faint" role="img" aria-label="Faint sketch of an anatomical heart with roses"></div>
    <div class="message-area"></div>
    <div class="stamp-box">Place<br>stamp<br>here</div>
    <div class="address-lines"><span></span><span></span><span></span></div>
  </div>
</section>

</body>
</html>
```